Adept Corvana Recruitment company

We require a website for job recruitment company called "Adept Corvana"
Our company is specialising in recruitment of skilled labour from Sri Lanka into Australian market.
We would like to include a job advertising plugin where jobs can be listed and applied for .
COPYWRITING MUST BE INCLUDED !

Industry/Entity Type

Recruitment

Coding

Coded - Design and coding required

Number of Pages Required

5+ page

Colors

Designer to choose colors to be used in the design.

```html
<!DOCTYPE html>
<html lang="en">
<head>
<meta charset="utf-8">
<title>Adept Corvana – Industrial Recruitment</title>
<link href="https://fonts.googleapis.com/css2?family=Roboto:ital,wght@0,300;0,400;0,500;0,700;1,400&display=swap" rel="stylesheet">
<style>
:root{
  --blue:#0a4ea6;
  --blue-dark:#073b82;
  --ink:#2b2b2b;
  --light:#f4f4f4;
  --grey:#e9e9ea;
  --btn-grey:#555a60;
  --white:#ffffff;
}
*{box-sizing:border-box;margin:0;padding:0}
html,body{width:1200px;height:4199px;overflow:hidden;background:var(--white)}
body{position:relative;font-family:'Roboto',sans-serif;color:var(--ink)}
.abs{position:absolute}
.btn{position:absolute;height:30px;border-radius:15px;color:var(--white);font-size:11px;font-weight:500;display:flex;align-items:center;justify-content:center}
.btn-blue{background:var(--blue)}
.btn-grey{background:var(--btn-grey)}
.brand{font-size:38px;font-weight:500;color:var(--ink);letter-spacing:.5px}
.section-title{position:absolute;left:0;width:1200px;text-align:center;font-size:24px;font-weight:400;color:var(--ink)}
.section-title b{color:var(--blue);font-weight:500}
.nav a{position:absolute;top:114px;font-size:10px;color:#444;text-decoration:none}
.nav a.active{color:var(--blue)}
.photo{position:absolute}
.copy{font-size:10.5px;line-height:17px;color:#555}
/* job cards */
.job-card{position:absolute;top:1287px;width:212px;height:300px;background:var(--white);box-shadow:0 4px 14px rgba(0,0,0,.08)}
.job-card .photo{left:0;top:0;width:212px;height:130px;background:linear-gradient(135deg,#8a7560,#c9a27a 45%,#4a5566)}
.job-card .role{position:absolute;left:0;top:98px;width:212px;height:32px;background:rgba(40,40,40,.75);color:#fff;font-size:11.5px;font-weight:500;padding:9px 14px}
.job-card h4{position:absolute;left:15px;top:146px;font-size:10.5px;font-weight:500;color:#333}
.job-card p{position:absolute;left:15px;top:166px;width:182px;font-size:8.5px;line-height:13px;color:#666}
.job-card .link{position:absolute;left:15px;top:226px;font-size:8.5px;color:#999;text-decoration:underline}
.job-card .btn{left:10px;top:256px;width:80px;height:26px}
/* steps */
.step{position:absolute;top:1938px;width:150px;text-align:center}
.step .ring{width:76px;height:76px;margin:0 auto;border-radius:50%;border:2px solid var(--blue);background:#fff;position:relative;display:flex;align-items:center;justify-content:center}
.step .num{position:absolute;left:28px;bottom:-9px;width:16px;height:16px;border-radius:50%;background:var(--blue);color:#fff;font-size:8px;display:flex;align-items:center;justify-content:center}
.step h5{margin-top:22px;font-size:10.5px;font-weight:500;color:#333}
.step p{margin-top:8px;font-size:9px;line-height:14px;color:#666}
/* blogs */
.blog-card{position:absolute;top:3286px;width:160px;height:240px;background:#fff;box-shadow:0 4px 14px rgba(0,0,0,.08)}
.blog-card .photo{left:0;top:0;width:160px;height:80px}
.blog-card .by{position:absolute;left:15px;top:94px;font-size:8.5px;color:var(--blue);font-weight:500}
.blog-card h4{position:absolute;left:15px;top:110px;width:132px;font-size:10px;line-height:14px;font-weight:500;color:#333}
.blog-card p{position:absolute;left:15px;top:148px;width:132px;font-size:8.5px;line-height:13px;color:#666}
.blog-card .go{position:absolute;left:18px;top:228px;width:22px;height:22px;border-radius:50%;background:var(--btn-grey);display:flex;align-items:center;justify-content:center}
.blog-card .go.on{background:var(--blue)}
/* footer */
.foot-links a{display:block;font-size:10px;color:#555;text-decoration:none;height:25px}
.social{position:absolute;top:3976px;width:28px;height:28px;border-radius:50%;background:#b8b8bb}
.social.on{background:var(--blue)}
</style>
</head>
<body>

<header>
  <div class="abs brand" style="left:148px;top:62px">Adept Corvana</div>
  <div class="abs" style="left:708px;top:67px;font-size:11px;color:#444"><span style="color:var(--blue)">Call Us:</span>
    <svg width="10" height="10" viewBox="0 0 24 24" style="vertical-align:-1px"><path fill="#0a4ea6" d="M6.6 10.8a15 15 0 0 0 6.6 6.6l2.2-2.2c.3-.3.7-.4 1-.2 1.1.4 2.3.6 3.6.6.6 0 1 .4 1 1V20c0 .6-.4 1-1 1A17 17 0 0 1 3 4c0-.6.4-1 1-1h3.5c.6 0 1 .4 1 1 0 1.3.2 2.5.6 3.6.1.3 0 .7-.2 1z"/></svg>
    555-014-2290</div>
  <div class="btn btn-blue" style="left:928px;top:60px;width:122px">Consult Now</div>
  <nav class="nav">
    <a class="active" style="left:474px">– Home –</a>
    <a style="left:540px">About Us</a>
    <a style="left:600px">For Employees</a>
    <a style="left:686px">For Employers</a>
    <a style="left:770px">Testimonials</a>
    <a style="left:846px">Blogs</a>
    <a style="left:893px">Contact Us</a>
  </nav>
</header>

<section class="hero">
  <div class="photo" role="img" aria-label="Blue-tinted photo of hands typing on a laptop keyboard" style="left:150px;top:144px;width:900px;height:380px;background:linear-gradient(120deg,#1f5aa6 0%,#2e6cb6 45%,#5b8cc7 75%,#2a62ad 100%)"></div>
  <svg class="abs" style="left:150px;top:380px" width="900" height="150" viewBox="0 0 900 150">
    <path d="M0 70 C180 10 330 30 470 60 C620 92 760 70 900 40 L900 150 L0 150Z" fill="#7fa4d3" opacity=".55"/>
    <path d="M0 95 C200 35 340 55 480 85 C640 118 780 95 900 65 L900 150 L0 150Z" fill="#c9d9ee"/>
    <path d="M0 115 C200 60 350 80 500 110 C660 140 800 115 900 90 L900 150 L0 150Z" fill="#fff"/>
  </svg>
  <h1 class="abs" style="left:150px;top:236px;width:900px;text-align:center;font-size:29px;font-weight:300;color:#fff">Looking for Industrial <b style="font-weight:500">Job?</b></h1>
  <div class="abs" style="left:335px;top:302px;width:218px;height:32px;border-radius:16px;background:#fff;font-size:10px;color:#555;padding:10px 16px">Location<span style="position:absolute;right:16px">▾</span></div>
  <div class="abs" style="left:556px;top:302px;width:218px;height:32px;border-radius:16px;background:#fff;font-size:10px;color:#555;padding:10px 16px">Skills<span style="position:absolute;right:16px">▾</span></div>
  <div class="btn btn-blue" style="left:786px;top:302px;width:78px;height:32px;border:2px solid #fff">Search</div>
  <svg class="abs" style="left:594px;top:446px" width="12" height="16" viewBox="0 0 12 16"><path d="M6 1v13M1 9l5 5 5-5" stroke="#333" stroke-width="1.4" fill="none"/></svg>
</section>

<section class="about">
  <h2 class="abs" style="left:335px;top:646px;font-size:21px;font-weight:400;color:#333">Adept <span style="color:var(--blue)">Corvana</span></h2>
  <div class="abs copy" style="left:335px;top:696px;width:245px">
    <p>We connect skilled tradespeople from Sri Lanka with trusted Australian employers. Our team screens every candidate, checks each trade licence and prepares workers for site life, so that both sides start with confidence from the very first day on the job.</p>
    <p style="margin-top:17px">From welders and fitters to machine operators, we guide each step of hiring and relocation with care and clear advice.</p>
  </div>
  <div class="btn btn-grey" style="left:335px;top:958px;width:80px">About Us</div>
  <div class="photo" role="img" aria-label="Photo of business people signing documents at a desk" style="left:599px;top:594px;width:266px;height:340px;background:linear-gradient(160deg,#e8e4df 0%,#b9aa98 40%,#6d5b4a 70%,#d8d2ca 100%)"></div>
</section>

<section class="jobs">
  <svg class="abs" style="left:150px;top:1060px" width="900" height="760" viewBox="0 0 900 760">
    <path d="M0 30 C120 0 230 -5 360 25 C520 60 700 40 900 10 L900 760 L0 760Z" fill="var(--light)"/>
  </svg>
  <h2 class="section-title" style="top:1222px">Job <b>opportunities</b></h2>

  <article class="job-card" style="left:262px">
    <div class="photo" role="img" aria-label="Photo of a production supervisor inspecting machinery"></div>
    <div class="role">Production Supervisor</div>
    <h4>Job Description:</h4>
    <p>Lead a shift team on a busy factory floor, track daily output, keep safety high and report to the plant manager ...</p>
    <span class="link">www.corvanajobs.example</span>
    <div class="btn btn-grey">Read More</div>
  </article>
  <article class="job-card" style="left:497px">
    <div class="photo" role="img" aria-label="Photo of a smiling salesperson in a retail store" style="background:linear-gradient(135deg,#a0552f,#d88a3a 40%,#3f6aa0)"></div>
    <div class="role">Salesman</div>
    <h4>Job Description:</h4>
    <p>Build strong client relationships, present our industrial products clearly and meet monthly sales goals ...</p>
    <span class="link">www.corvanajobs.example</span>
    <div class="btn btn-blue">Read More</div>
  </article>
  <article class="job-card" style="left:728px">
    <div class="photo" role="img" aria-label="Photo of an industrial engineer in a hard hat on site" style="background:linear-gradient(135deg,#6b7480,#c7a064 45%,#5c6470)"></div>
    <div class="role">Industrial Engineer</div>
    <h4>Job Description:</h4>
    <p>Design better workflows for production lines, study equipment data and help cut waste while keeping quality ...</p>
    <span class="link">www.corvanajobs.example</span>
    <div class="btn btn-grey">Read More</div>
  </article>

  <div class="btn btn-blue" style="left:560px;top:1640px;width:80px">View All</div>
</section>

<section class="process">
  <h2 class="section-title" style="top:1884px">One stop for your industrial <b>skilled people</b></h2>
  <div class="step" style="left:212px">
    <div class="ring"><svg width="26" height="26" viewBox="0 0 24 24" fill="none" stroke="#444" stroke-width="1.2"><rect x="3" y="4" width="18" height="16" rx="1"/><path d="M7 8h10M7 12h4M7 16h4M13 12h4v4h-4z"/></svg><span class="num">1</span></div>
    <h5>Advertise job posts</h5><p>We share your openings with a wide talent pool.</p>
  </div>
  <div class="step" style="left:368px">
    <div class="ring"><svg width="26" height="26" viewBox="0 0 24 24" fill="none" stroke="#444" stroke-width="1.2"><path d="M6 3h9l4 4v14H6z"/><path d="M9 10h7M9 13h7M9 16h7"/></svg><span class="num">2</span></div>
    <h5>Collect applications</h5><p>All applications are gathered and sorted for you.</p>
  </div>
  <div class="step" style="left:525px">
    <div class="ring"><svg width="26" height="26" viewBox="0 0 24 24" fill="none" stroke="#444" stroke-width="1.2"><rect x="5" y="4" width="14" height="17" rx="1"/><path d="M9 3h6v3H9zM8 10h8M8 13h8M8 16h8"/></svg><span class="num">3</span></div>
    <h5>Shortlist candidates</h5><p>Only the best skills reach your interview list.</p>
  </div>
  <div class="step" style="left:681px">
    <div class="ring"><svg width="26" height="26" viewBox="0 0 24 24" fill="none" stroke="#444" stroke-width="1.2"><path d="M2 10l5-4 5 3 5-3 5 4-6 6-4-3-4 3z"/><path d="M9 13l3 3"/></svg><span class="num">4</span></div>
    <h5>Organize interviews</h5><p>We book meetings that suit both sides well.</p>
  </div>
  <div class="step" style="left:839px">
    <div class="ring"><svg width="30" height="26" viewBox="0 0 28 24" fill="none" stroke="#444" stroke-width="1.3"><path d="M2 13l5 5 11-12M10 17l1 1 13-13"/></svg><span class="num">5</span></div>
    <h5>Get permits &amp; immigration</h5><p>Visa paperwork is handled until arrival day.</p>
  </div>
  <div class="btn btn-blue" style="left:553px;top:2140px;width:94px">Consult Now</div>
</section>

<section class="cta">
  <svg class="abs" style="left:150px;top:2240px" width="900" height="940" viewBox="0 0 900 940">
    <defs>
      <linearGradient id="ctaFill" x1="0" y1="0" x2="1" y2="1">
        <stop offset="0" stop-color="#0b4fa8"/><stop offset=".6" stop-color="#0a479a"/><stop offset="1" stop-color="#093d86"/>
      </linearGradient>
    </defs>
    <rect x="0" y="380" width="900" height="560" fill="var(--grey)"/>
    <path d="M0 110 C120 30 260 -10 420 30 C560 70 660 120 760 110 C830 100 870 80 900 70 L900 470 C800 500 700 440 600 420 C480 400 390 470 250 460 C150 452 70 420 0 440Z" fill="url(#ctaFill)" role="img" aria-label="Blue-tinted photo of a city crowd"/>
    <path d="M0 440 C70 420 150 452 250 460 C390 470 480 400 600 420 C700 440 800 500 900 470 L900 520 C780 560 650 470 560 470 C430 470 360 540 220 520 C120 505 60 470 0 480Z" fill="#fff" opacity=".9"/>
  </svg>
  <div class="abs" role="img" aria-label="Illustration of a businessman figure" style="left:785px;top:2440px;width:60px;height:150px;background:linear-gradient(#fff,#e8eef7);border-radius:30px 30px 4px 4px"></div>
  <h2 class="abs" style="left:335px;top:2412px;width:420px;font-size:27px;line-height:31px;font-weight:300;color:#fff">Are you Skilled with Industrial work and <b style="font-weight:500">Dream to Fly</b> all the way <b style="font-weight:500">to Australia?</b></h2>
  <div class="btn" style="left:335px;top:2558px;width:90px;background:#fff;color:var(--blue)">Submit Details</div>

  <h2 class="section-title" style="top:2752px">Happy <b>clients say</b></h2>
  <div class="abs" style="left:570px;top:2818px;width:60px;height:60px;border-radius:50%;border:2px solid var(--blue);display:flex;align-items:center;justify-content:center">
    <div style="width:44px;height:44px;border-radius:50%;background:var(--blue);display:flex;align-items:center;justify-content:center;color:#fff;font-size:26px;font-weight:700;line-height:1">“</div>
  </div>
  <p class="abs" style="left:350px;top:2906px;width:500px;text-align:center;font-size:10.5px;line-height:17px;color:#666;font-style:italic">" Working with this team was simple from start to finish. They understood the skills we needed, sent a strong shortlist within weeks and kept us informed during every visa step. Our new welders settled in quickly and fit the crew well. "</p>
  <div class="abs" style="left:0;top:2996px;width:1200px;text-align:center;font-size:11px;color:var(--blue);font-weight:500">Mira Delacott</div>
  <div class="abs" style="left:0;top:3014px;width:1200px;text-align:center;font-size:9px;color:#777">Salesman</div>
  <div class="btn btn-grey" style="left:560px;top:3064px;width:80px">View All</div>
  <svg class="abs" style="left:258px;top:2930px" width="12" height="20" viewBox="0 0 12 20"><path d="M10 1L2 10l8 9" stroke="#0a4ea6" stroke-width="1.5" fill="none"/></svg>
  <svg class="abs" style="left:928px;top:2930px" width="12" height="20" viewBox="0 0 12 20"><path d="M2 1l8 9-8 9" stroke="#0a4ea6" stroke-width="1.5" fill="none"/></svg>
</section>

<section class="blogs">
  <h2 class="section-title" style="top:3230px">Latest <b>blogs</b></h2>
  <article class="blog-card" style="left:335px">
    <div class="photo" role="img" aria-label="Photo of construction workers on scaffolding at sunset" style="background:linear-gradient(135deg,#d9a35c,#6d7f95)"></div>
    <span class="by">By Nalin Perera</span>
    <h4>Preparing for your first Australian site job</h4>
    <p>Simple tips on tools, safety cards and daily routines that help new arrivals settle in ...</p>
    <span class="go"><svg width="10" height="10" viewBox="0 0 10 10"><path d="M1 5h8M5 1l4 4-4 4" stroke="#fff" stroke-width="1.3" fill="none"/></svg></span>
  </article>
  <article class="blog-card" style="left:520px">
    <div class="photo" role="img" aria-label="Photo of a welder working with sparks" style="background:linear-gradient(135deg,#e09a3e,#7a6a5c)"></div>
    <span class="by">By Nalin Perera</span>
    <h4>Trade skills most wanted this year</h4>
    <p>A look at the roles employers are hiring for now, from fitters to plant operators ...</p>
    <span class="go on"><svg width="10" height="10" viewBox="0 0 10 10"><path d="M1 5h8M5 1l4 4-4 4" stroke="#fff" stroke-width="1.3" fill="none"/></svg></span>
  </article>
  <article class="blog-card" style="left:706px">
    <div class="photo" role="img" aria-label="Photo of a mechanic working on an engine" style="background:linear-gradient(135deg,#9aa4ae,#3f464e)"></div>
    <span class="by">By Nalin Perera</span>
    <h4>How the skilled visa process works</h4>
    <p>A clear guide to permits, checks and timelines so you know what to expect next ...</p>
    <span class="go"><svg width="10" height="10" viewBox="0 0 10 10"><path d="M1 5h8M5 1l4 4-4 4" stroke="#fff" stroke-width="1.3" fill="none"/></svg></span>
  </article>
  <div class="btn btn-grey" style="left:553px;top:3600px;width:94px">View All Blog</div>
</section>

<footer>
  <svg class="abs" style="left:150px;top:3720px" width="900" height="479" viewBox="0 0 900 479">
    <path d="M0 40 C150 0 260 10 380 40 C540 80 700 20 900 30 L900 479 L0 479Z" fill="var(--grey)"/>
  </svg>
  <div class="abs brand" style="left:148px;top:3890px">Adept Corvana</div>
  <span class="social" style="left:192px"></span>
  <span class="social on" style="left:235px"></span>
  <span class="social" style="left:279px"></span>

  <div class="abs" style="left:473px;top:3878px">
    <h6 style="font-size:11px;font-weight:500;color:#333;margin-bottom:16px">Quick Links</h6>
    <nav class="foot-links"><a>Home</a><a>About Us</a><a>For Employees</a><a>For Employers</a><a>Testimonials</a><a>Blogs</a><a>Contact Us</a></nav>
  </div>
  <div class="abs" style="left:684px;top:3878px;font-size:11px;font-weight:500;color:#333">Sign Up Newsletter</div>
  <div class="abs" style="left:668px;top:3918px;width:382px;height:32px;border-radius:16px;border:1px solid #aaa;background:#fff;font-size:10px;color:#777;padding:10px 18px">Enter your Email ...</div>
  <div class="btn btn-blue" style="left:668px;top:3966px;width:106px">Submit</div>

  <div class="abs" style="left:148px;top:4087px;width:902px;height:1px;background:#c9c9cb"></div>
  <div class="abs" style="left:148px;top:4114px;font-size:10px;color:#555">© 2022 <span style="color:var(--blue)">Adept Corvana</span> &nbsp;|&nbsp; All Right Reserved</div>
  <svg class="abs" style="left:1112px;top:4104px" width="20" height="24" viewBox="0 0 20 24"><path d="M10 1L19 23 10 17 1 23z" fill="#0a4ea6"/></svg>
</footer>

</body>
</html>
```